Tobias Wrenfield Business Card

In addition to my name design (file uploaded), black print on white card stock, e-mail address should be presented as a typical e-mail address, i.e., underlined and in blue ink, the card should include the following information:
Professor of Flight Operations
Aircraft Incident Expert Consultant
Senior Certified Flight Instructor

twrenfield@qorvanet.net
Kenai, Alaska
(907) 518-2736

Industry/Entity Type

Business

```html
<!DOCTYPE html>
<html lang="en">
<head>
<meta charset="utf-8">
<title>Tobias Wrenfield Business Card</title>
<link rel="stylesheet" href="https://fonts.googleapis.com/css2?family=Arimo:wght@400;700&family=Oswald:wght@600&display=swap">
<style>
  :root {
    --backdrop: #606167;
    --card: #fbfbf9;
    --ink: #111111;
    --rule-blue: #3a86cc;
    --link-blue: #1f6fd0;
    --plane-grey: #8f8f8f;
    --plane-light: #a9a9a9;
  }
  * { box-sizing: border-box; margin: 0; padding: 0; }
  html, body {
    width: 1200px; height: 928px; overflow: hidden;
    background: var(--backdrop);
    font-family: "Arimo", Arial, sans-serif;
    color: var(--ink);
  }
  .canvas { position: relative; width: 1200px; height: 928px; }
  .card {
    position: absolute; top: 269px;
    width: 540px; height: 390px;
    background: var(--card);
    overflow: hidden;
  }
  .card--front { left: 45px; }
  .card--back { left: 615px; }

  .wordmark {
    position: absolute;
    font-family: "Oswald", "Arial Narrow", sans-serif;
    font-weight: 600;
    line-height: 1;
    letter-spacing: 1px;
    text-transform: uppercase;
    color: var(--ink);
    white-space: nowrap;
  }
  .card--front .wordmark { left: 70px; top: 32px; font-size: 40px; }
  .card--back .wordmark { left: 100px; top: 120px; font-size: 44px; }

  .rule { position: absolute; height: 4px; background: var(--rule-blue); }
  .card--front .rule { left: 8px; right: 0; top: 90px; }
  .card--back .rule { left: 80px; right: 0; top: 96px; }

  .plane-mark {
    position: absolute;
    border-radius: 50%;
    background: radial-gradient(circle, var(--plane-light) 0%, rgba(169,169,169,0.35) 55%, rgba(169,169,169,0) 72%);
  }
  .plane-mark--large {
    background: radial-gradient(circle, var(--plane-grey) 0%, rgba(143,143,143,0.4) 55%, rgba(143,143,143,0) 72%);
  }

  .credentials { position: absolute; left: 38px; top: 178px; }
  .credentials__title { font-size: 19px; line-height: 1.2; }
  .credentials__line { font-size: 13px; line-height: 1.55; margin-left: 6px; }

  .contact { position: absolute; left: 54px; top: 292px; font-size: 17px; line-height: 1.3; }
  .contact__email { color: var(--link-blue); text-decoration: underline; }
</style>
</head>
<body>
<main class="canvas">

  <section class="card card--front" aria-label="Card front">
    <div class="plane-mark" role="img" aria-label="Small airplane silhouette" style="left:450px;top:26px;width:46px;height:46px"></div>
    <div class="plane-mark" role="img" aria-label="Small airplane silhouette" style="left:370px;top:112px;width:44px;height:44px"></div>
    <div class="plane-mark plane-mark--large" role="img" aria-label="Large airplane silhouette" style="left:335px;top:180px;width:84px;height:84px"></div>
    <div class="plane-mark" role="img" aria-label="Small airplane silhouette" style="left:310px;top:315px;width:26px;height:26px"></div>
    <div class="plane-mark" role="img" aria-label="Small airplane silhouette" style="left:8px;top:342px;width:40px;height:40px"></div>

    <div class="wordmark">Tobias Wrenfield</div>
    <div class="rule"></div>

    <div class="credentials">
      <p class="credentials__title">Professor of Flight Operations</p>
      <p class="credentials__line">Aircraft Incident Expert Consultant</p>
      <p class="credentials__line">Senior Certified Flight Instructor</p>
    </div>

    <div class="contact">
      <p class="contact__email">twrenfield@qorvanet.net</p>
      <p class="contact__city">Kenai, Alaska</p>
      <p class="contact__phone">(907) 518-2736</p>
    </div>
  </section>

  <section class="card card--back" aria-label="Card back">
    <div class="plane-mark" role="img" aria-label="Small airplane silhouette" style="left:115px;top:38px;width:50px;height:50px"></div>
    <div class="plane-mark" role="img" aria-label="Small airplane silhouette" style="left:470px;top:28px;width:50px;height:50px"></div>
    <div class="plane-mark" role="img" aria-label="Small airplane silhouette" style="left:22px;top:125px;width:30px;height:30px"></div>
    <div class="plane-mark" role="img" aria-label="Small airplane silhouette" style="left:140px;top:200px;width:26px;height:26px"></div>
    <div class="plane-mark plane-mark--large" role="img" aria-label="Large airplane silhouette" style="left:220px;top:195px;width:95px;height:95px"></div>
    <div class="plane-mark plane-mark--large" role="img" aria-label="Small airplane silhouette" style="left:400px;top:215px;width:40px;height:40px"></div>
    <div class="plane-mark" role="img" aria-label="Small airplane silhouette" style="left:110px;top:272px;width:48px;height:48px"></div>
    <div class="plane-mark" role="img" aria-label="Small airplane silhouette" style="left:325px;top:330px;width:26px;height:26px"></div>
    <div class="plane-mark" role="img" aria-label="Small airplane silhouette" style="left:480px;top:330px;width:32px;height:32px"></div>
    <div class="plane-mark" role="img" aria-label="Small airplane silhouette" style="left:30px;top:345px;width:46px;height:46px"></div>

    <div class="rule"></div>
    <div class="wordmark">Tobias Wrenfield</div>
  </section>

</main>
</body>
</html>
```